Framed Poster for my Home- song lyrics

Poster with song lyrics by the Varlow. The lyrics need to be printed onto paper- needs to be very high quality and then I want to have it framed

size 11x17

Show me Show Me Show Me How You Do That Trick...

Target Market(s)

Self

Font styles to use
Serif

Colors
85acd3
f68d4d
f37122

Requirements
Must have
• Great Font and needs to be a very High quality poster-- it will be framed
Nice to have
• Color-- and a design behind the lyrics

```html
<!DOCTYPE html>
<html lang="en">
<head>
<meta charset="UTF-8">
<title>Show Me How You Do That Trick — Lyric Poster</title>
<link rel="stylesheet" href="https://fonts.googleapis.com/css2?family=Righteous&family=Bungee+Inline&family=Poppins:wght@800&display=swap">
<style>
  :root {
    --sky: #8faad2;
    --slate: #43536d;
    --orange: #d8702e;
    --white: #ffffff;
  }
  html, body {
    margin: 0;
    padding: 0;
    width: 870px;
    height: 1200px;
    overflow: hidden;
    background: var(--sky);
  }
  .poster {
    display: block;
    width: 870px;
    height: 1200px;
  }
  .poster__sky { fill: var(--sky); }
  .poster__shadow { fill: var(--slate); }
  .lyric {
    font-family: "Righteous", "Poppins", sans-serif;
  }
  .lyric--inline {
    font-family: "Bungee Inline", "Righteous", sans-serif;
  }
  .lyric--orange { fill: var(--orange); }
  .lyric--white { fill: var(--white); }
  .credit {
    font-family: "Poppins", sans-serif;
    font-weight: 800;
    fill: var(--orange);
  }
</style>
</head>
<body>
<svg class="poster" viewBox="0 0 870 1200" xmlns="http://www.w3.org/2000/svg" role="img" aria-label="Lyric poster: Show me, show me, show me how you do that trick, by the Varlow">
  <rect class="poster__sky" x="0" y="0" width="870" height="1200"/>
  <polygon class="poster__shadow"
    points="168,95 829,95 870,148 870,1200 190,1200 40,1042 31,829 33,366 109,347 109,228 168,204"/>

  <text class="lyric lyric--orange" x="168" y="204" font-size="160" textLength="661" lengthAdjust="spacingAndGlyphs">SHOWME</text>
  <text class="lyric lyric--white" x="109" y="347" font-size="170" textLength="722" lengthAdjust="spacingAndGlyphs">SHOWME</text>
  <text class="lyric lyric--orange" x="33" y="499" font-size="190" textLength="801" lengthAdjust="spacingAndGlyphs">SHOWME</text>
  <text class="lyric lyric--white" x="33" y="650" font-size="182" textLength="803" lengthAdjust="spacingAndGlyphs">HOW YOU</text>
  <text class="lyric lyric--white" x="31" y="829" font-size="202" textLength="268" lengthAdjust="spacingAndGlyphs">DO</text>
  <text class="lyric lyric--inline lyric--orange" x="357" y="829" font-size="192" textLength="479" lengthAdjust="spacingAndGlyphs">THAT</text>
  <text class="lyric lyric--inline lyric--orange" x="27" y="1042" font-size="248" textLength="809" lengthAdjust="spacingAndGlyphs">TRICK</text>

  <text class="credit" x="836" y="1143" font-size="36" text-anchor="end">BY THE VARLOW</text>
</svg>
</body>
</html>
```